Website visual upgrade

I am seeking expressions of interest for the updating the visuals of my website www.lunvaleplacements.example
I am basically seeking a simple,bold and visually strong graphic makeover.using existing or shortly to be modified text.

```html
<!DOCTYPE html>
<html lang="en">
<head>
<meta charset="utf-8">
<title>Lunvale Placements — Home</title>
<link rel="stylesheet" href="https://fonts.googleapis.com/css2?family=Roboto:wght@300;400;500&display=swap">
<style>
  :root {
    --header-top: #5b5b5b;
    --header-bottom: #2f2f2f;
    --footer-bg: #2c2c2c;
    --accent-red: #c4122f;
    --nav-text: #e6e6e6;
    --muted-text: #bdbdbd;
    --white: #ffffff;
    --logo-bg-light: #f7f7f7;
    --logo-bg-dark: #e2e2e2;
    --brand-red: #b5122e;
    --icon-grey: #9a9a9a;
    --sky-top: #6a9ccf;
    --sky-bottom: #a9c8e6;
    --shirt-teal: #2fa7c9;
  }
  * { margin: 0; padding: 0; box-sizing: border-box; }
  html, body { width: 1200px; height: 741px; overflow: hidden; }
  body {
    position: relative;
    font-family: "Roboto", Arial, sans-serif;
    background: var(--footer-bg);
  }

  .site-header {
    position: absolute; left: 0; top: 0; width: 1200px; height: 146px;
    background: linear-gradient(to bottom, var(--header-top), var(--header-bottom));
    box-shadow: 0 2px 6px rgba(0,0,0,0.5);
    z-index: 2;
  }
  .brand {
    position: absolute; left: 66px; top: 0; width: 355px; height: 84px;
    background: linear-gradient(to bottom, var(--logo-bg-light), var(--logo-bg-dark));
    display: flex; align-items: center; padding-left: 16px; gap: 14px;
  }
  .brand-dot { width: 40px; height: 40px; border-radius: 50%; background: #2a2a2a; flex: none; }
  .brand-name {
    font-weight: 500; font-size: 27px; color: var(--brand-red); letter-spacing: 0.2px;
  }

  .social {
    position: absolute; right: 68px; top: 20px; display: flex; align-items: center; gap: 10px;
  }
  .social-label { font-size: 13px; font-weight: 300; color: var(--muted-text); margin-right: 2px; }
  .social-dot { width: 31px; height: 31px; border-radius: 50%; background: var(--icon-grey); }

  .main-nav { position: absolute; left: 0; top: 107px; width: 1200px; }
  .main-nav a {
    position: absolute; top: 0; font-size: 13.6px; color: var(--nav-text);
    text-decoration: none; text-transform: uppercase; letter-spacing: 0.2px; white-space: nowrap;
  }
  .nav-active-marker {
    position: absolute; left: 64px; top: 139px; width: 66px; height: 7px;
  }

  .hero {
    position: absolute; left: 0; top: 146px; width: 1200px; height: 480px;
    overflow: hidden;
  }
  .hero-photo {
    position: absolute; inset: 0;
    background:
      radial-gradient(ellipse 260px 320px at 790px 380px, rgba(47,167,201,0.55), rgba(47,167,201,0) 70%),
      linear-gradient(to bottom, var(--sky-top), var(--sky-bottom));
  }
  .hero-title {
    position: absolute; left: 62px; top: 96px;
    font-size: 70px; font-weight: 400; line-height: 72px; color: var(--white);
    text-shadow: 0 2px 4px rgba(0,0,0,0.25); letter-spacing: 0.5px;
  }
  .hero-controls { position: absolute; left: 68px; top: 349px; display: flex; gap: 9px; }
  .hero-controls svg { display: block; }

  .hero-rule { position: absolute; left: 0; top: 626px; width: 1200px; height: 2px; background: var(--accent-red); }

  .site-footer { position: absolute; left: 0; top: 628px; width: 1200px; height: 113px; background: var(--footer-bg); }
  .copyright { position: absolute; left: 66px; top: 36px; font-size: 11.5px; color: var(--muted-text); }
  .copyright strong { font-weight: 400; color: var(--white); }
  .footer-links { position: absolute; left: 66px; top: 62px; font-size: 11.5px; color: var(--muted-text); }
  .footer-links a { color: var(--muted-text); text-decoration: none; }
  .footer-links .sep { margin: 0 5px; }
  .supporters-label { position: absolute; left: 923px; top: 14px; font-size: 13px; font-weight: 300; color: var(--nav-text); }
  .supporter-badge { position: absolute; top: 39px; height: 54px; }
  .supporter-badge.wide { left: 925px; width: 135px; background: #f4f0ea; }
  .supporter-badge.square { left: 1080px; width: 52px; background: #0d0d0d; }
</style>
</head>
<body>
  <header class="site-header">
    <div class="brand">
      <span class="brand-dot"></span>
      <span class="brand-name">Lunvale Placements</span>
    </div>
    <div class="social">
      <span class="social-label">We Proudly Support:</span>
      <span class="social-dot" aria-label="Social profile"></span>
      <span class="social-dot" aria-label="Social profile"></span>
    </div>
    <nav class="main-nav">
      <a href="#" style="left:76px;color:var(--white)">Home</a>
      <a href="#" style="left:146px">Who We Are</a>
      <a href="#" style="left:262px">Our Approach</a>
      <a href="#" style="left:398px">What We Do</a>
      <a href="#" style="left:516px">Migration Assistance</a>
      <a href="#" style="left:709px">Job Seekers</a>
      <a href="#" style="left:827px">Useful Links</a>
      <a href="#" style="left:948px">Support</a>
      <a href="#" style="left:1038px">Contact Us</a>
    </nav>
    <svg class="nav-active-marker" viewBox="0 0 66 7" aria-hidden="true">
      <polygon points="0,3 26,3 33,0 40,3 66,3 66,7 0,7" fill="var(--accent-red)"/>
    </svg>
  </header>

  <section class="hero">
    <div class="hero-photo" role="img" aria-label="Smiling engineer in a white hard hat and teal polo shirt, arms folded, in front of a wind turbine against a blue sky"></div>
    <h1 class="hero-title">Local Presence,<br>Global Reach</h1>
    <div class="hero-controls">
      <svg width="32" height="32" viewBox="0 0 32 32" aria-label="Previous slide">
        <circle cx="16" cy="16" r="15" fill="#f2f2f2" stroke="#bbb"/>
        <polyline points="19,9 12,16 19,23" fill="none" stroke="#333" stroke-width="3"/>
      </svg>
      <svg width="32" height="32" viewBox="0 0 32 32" aria-label="Next slide">
        <circle cx="16" cy="16" r="15" fill="#f2f2f2" stroke="#bbb"/>
        <polyline points="13,9 20,16 13,23" fill="none" stroke="#333" stroke-width="3"/>
      </svg>
    </div>
  </section>
  <div class="hero-rule"></div>

  <footer class="site-footer">
    <p class="copyright">Copyright ©2013. <strong>Lunvale Placements</strong></p>
    <p class="footer-links">
      <a href="#">All Right Reserved</a><span class="sep">|</span><a href="#">Privacy Policy</a><span class="sep">|</span><a href="#">Site Map</a>
    </p>
    <p class="supporters-label">We Proudly Support:</p>
    <div class="supporter-badge wide" aria-label="Supported charity"></div>
    <div class="supporter-badge square" aria-label="Supported charity"></div>
  </footer>
</body>
</html>
```